Real Estate Sales Representative need a Billboard

I need a billboard for a Real Estate Sales Representative for Brisk Halvern Morrow & Associates. His name is Derek Fallowby, Cell number: 613-555-0148. Maybe add in "Best Experience Guaranteed", "Award Winning Top Realtor", "Buying or Selling? Call..."

```html
<!DOCTYPE html>
<html lang="en">
<head>
<meta charset="utf-8">
<title>Derek Fallowby – Billboard</title>
<link href="https://fonts.googleapis.com/css2?family=Roboto:ital,wght@0,400;0,500;0,700;0,900;1,500&display=swap" rel="stylesheet">
<style>
  :root {
    --red: #d0121b;
    --red-dark: #a80c13;
    --ink: #1d1d1f;
    --band: #1a1a1a;
    --paper: #f1f1f1;
    --stage: #e4e6e9;
    --white: #ffffff;
    --grey: #6b6b6b;
  }
  * { box-sizing: border-box; margin: 0; padding: 0; }
  html, body { width: 896px; height: 1200px; overflow: hidden; }
  body {
    background: var(--stage);
    font-family: "Roboto", Arial, sans-serif;
    display: flex; align-items: center; justify-content: center;
  }
  .billboard {
    position: relative;
    width: 896px; height: 464px;
    background: linear-gradient(180deg, #fafafa 0%, var(--paper) 100%);
    overflow: hidden;
  }
  .headline-band {
    position: absolute; left: 0; top: 0; width: 100%; height: 142px;
    background: linear-gradient(180deg, var(--red) 0%, var(--red-dark) 100%);
    color: var(--white); text-align: center;
    padding-top: 12px;
  }
  .headline { font-weight: 900; font-size: 64px; line-height: 72px; letter-spacing: 0.5px; }
  .subhead { font-weight: 700; font-size: 34px; line-height: 42px; letter-spacing: 1px; }
  .agent-name {
    position: absolute; left: 30px; top: 152px;
    font-weight: 900; font-size: 62px; line-height: 68px;
    color: var(--red); letter-spacing: 0.5px;
  }
  .agent-title {
    position: absolute; left: 62px; top: 222px;
    font-weight: 500; font-style: italic; font-size: 34px; color: var(--ink);
  }
  .call-band {
    position: absolute; left: 0; top: 272px; width: 600px; height: 56px;
    background: var(--band); color: var(--white);
    display: flex; align-items: center; padding-left: 24px; gap: 16px;
    font-weight: 900; font-size: 42px; letter-spacing: 0.5px;
  }
  .call-icon { width: 44px; height: 44px; flex: none; }
  .affiliations {
    position: absolute; left: 24px; top: 346px; width: 572px; height: 100px;
    display: flex; align-items: center; gap: 22px;
  }
  .brokerage { display: flex; flex-direction: column; gap: 6px; width: 170px; }
  .brokerage-mark { display: flex; align-items: center; gap: 8px; }
  .brokerage-square { width: 22px; height: 22px; background: var(--red); }
  .brokerage-name { font-weight: 900; font-size: 20px; color: var(--red); }
  .brokerage-office { font-size: 11px; line-height: 14px; color: var(--grey); }
  .badge-plain { flex: none; }
  .agent-photo {
    position: absolute; left: 612px; top: 150px; width: 270px; height: 314px;
    background: linear-gradient(180deg, #c9cdd3 0%, #7f8792 55%, #2c3038 100%);
  }
</style>
</head>
<body>
  <section class="billboard">
    <header class="headline-band">
      <h1 class="headline">BUYING OR SELLING?</h1>
      <p class="subhead">BEST EXPERIENCE GUARANTEED</p>
    </header>

    <h2 class="agent-name">DEREK FALLOWBY</h2>
    <p class="agent-title">Award Winning Top Realtor</p>

    <div class="call-band">
      <svg class="call-icon" viewBox="0 0 44 44" aria-hidden="true">
        <circle cx="22" cy="22" r="22" fill="#d0121b"/>
        <path d="M15 12c1-1 2.5-1 3.3.2l2.4 3.4c.7 1 .5 2.3-.4 3.1l-1.6 1.3c1.2 2.6 3.2 4.6 5.8 5.8l1.3-1.6c.8-.9 2.1-1.1 3.1-.4l3.4 2.4c1.2.8 1.2 2.3.2 3.3l-1.8 1.8c-1.3 1.3-3.3 1.6-5 .8-5.4-2.6-9.7-6.9-12.3-12.3-.8-1.7-.5-3.7.8-5z" fill="#fff"/>
      </svg>
      <span class="call-text">CALL: 613-555-0148</span>
    </div>

    <div class="affiliations">
      <div class="brokerage">
        <div class="brokerage-mark">
          <span class="brokerage-square"></span>
          <span class="brokerage-name">BRISK HALVERN</span>
        </div>
        <p class="brokerage-office">Brisk Halvern Morrow &amp; Associates Brokerage</p>
      </div>
      <svg class="badge-plain" width="70" height="60" viewBox="0 0 70 60" aria-hidden="true">
        <rect x="2" y="8" width="66" height="44" fill="none" stroke="#b9b9b9" stroke-width="2"/>
      </svg>
      <svg class="badge-plain" width="72" height="72" viewBox="0 0 72 72" aria-hidden="true">
        <circle cx="36" cy="36" r="32" fill="none" stroke="#8c8c8c" stroke-width="3"/>
      </svg>
      <svg class="badge-plain" width="110" height="60" viewBox="0 0 110 60" aria-hidden="true">
        <rect x="2" y="10" width="106" height="40" fill="none" stroke="#8c8c8c" stroke-width="2"/>
      </svg>
      <svg class="badge-plain" width="80" height="60" viewBox="0 0 80 60" aria-hidden="true">
        <rect x="2" y="10" width="76" height="40" fill="none" stroke="#d0121b" stroke-width="2"/>
      </svg>
    </div>

    <div class="agent-photo" role="img" aria-label="Portrait photo of realtor Derek Fallowby in a dark suit"></div>
  </section>
</body>
</html>
```